Business Card Design Project

1. Show the company logo.
2. Only company email ID and website address to be shown (office@zolotoyveter.fm , www.zolotoyveter.fm).
3. Logo to be provided by us, 2 designs just in case. The logo is made with ' Zolotoy Veter' text, need to be edited so that it shows 'Tikhaya Gavan' instead .
4. Single sided business card, portrait or landscape is not a problem; back side to be filled with colors or a design that matches the logo the best.
5. Logo is to be embossed.
6. We're looking at an English and Russian version.
7. any other better idea is always welcomed.

```html
<!DOCTYPE html>
<html lang="en">
<head>
<meta charset="utf-8">
<title>Tikhaya Gavan — Business Card</title>
<link rel="stylesheet" href="https://fonts.googleapis.com/css2?family=Arimo:wght@400;700&display=swap">
<style>
  :root {
    --navy: #1e3868;
    --navy-deep: #1a3563;
    --sky: #22a3dc;
    --gold: #fcbd19;
    --paper-light: #f7f7f7;
    --paper-shade: #dedede;
    --text-light: #e9e9ec;
    --faint-circle: #c9d6e4;
    --trim-red: #e0453f;
    --trim-green: #4caf50;
  }
  html, body {
    margin: 0;
    padding: 0;
    overflow: hidden;
    background: #ffffff;
  }
  .card {
    position: relative;
    width: 1200px;
    height: 781px;
    overflow: hidden;
    background: radial-gradient(ellipse at 35% 30%, var(--paper-light) 0%, #ececec 55%, var(--paper-shade) 100%);
    font-family: "Arimo", Arial, sans-serif;
  }
  .card-art {
    position: absolute;
    inset: 0;
  }
  .brand-mark {
    position: absolute;
    left: 58px;
    top: 55px;
    width: 360px;
    height: 360px;
    border-radius: 50%;
    background: var(--navy);
    box-shadow: 4px 8px 14px rgba(0, 0, 0, 0.28);
    display: flex;
    align-items: center;
    justify-content: center;
  }
  .brand-name {
    margin: 0;
    color: var(--gold);
    font-weight: 700;
    font-size: 40px;
    line-height: 1.15;
    text-align: center;
    letter-spacing: 1px;
    text-transform: uppercase;
  }
  .contact {
    position: absolute;
    left: 0;
    right: 0;
    top: 648px;
    margin: 0;
    text-align: center;
    color: var(--text-light);
    font-weight: 700;
    font-size: 32px;
    line-height: 45px;
  }
  .trim-line {
    position: absolute;
    pointer-events: none;
  }
  .trim-line.bleed {
    inset: 4px;
    border: 1.5px solid var(--trim-red);
  }
  .trim-line.safe {
    inset: 12px;
    border: 1.5px solid var(--trim-green);
  }
</style>
</head>
<body>
<main class="card">
  <svg class="card-art" width="1200" height="781" viewBox="0 0 1200 781" aria-hidden="true">
    <circle class="backdrop-circle" cx="825" cy="250" r="250" fill="var(--faint-circle)" opacity="0.55"/>
    <path class="wave-gold" d="M560 520 C760 540 950 470 1200 360 L1200 610 C1000 600 800 580 560 560 Z" fill="var(--gold)"/>
    <path class="wave-sky" d="M0 590 C150 520 280 470 420 465 C600 460 700 520 860 525 C1000 528 1110 430 1200 340 L1200 560 C1100 575 1000 570 900 565 C750 555 600 505 430 495 C280 490 150 540 0 600 Z" fill="var(--sky)"/>
    <path class="wave-navy" d="M0 600 C150 540 280 490 430 495 C600 505 750 555 900 565 C1000 572 1100 585 1200 598 L1200 781 L0 781 Z" fill="var(--navy-deep)"/>
  </svg>

  <div class="brand-mark">
    <p class="brand-name">Tikhaya<br>Gavan</p>
  </div>

  <p class="contact">Our address :<br>office@zolotoyveter.fm , www.zolotoyveter.fm</p>

  <div class="trim-line bleed"></div>
  <div class="trim-line safe"></div>
</main>
</body>
</html>
```